Corporate Design + Logo Re-Launch Nordisches Elternschutzkreis
Zielgruppe
Das Nordischen Elternschutzkreis (NEKV) ist ein eingetragener Verein, der im Jahre 1982 gegründet wurde.
Das Nordische Elternschutzkreis eV ist den Rechten der Familie, insbesondere den Kindern verpflichtet. Von Anfang an unterhielt das nordische Elternschutzkreis eine Beratungsstelle in Stuttgart und entwickelte aus seiner jahrelangen betriebenen Tätigkeit ein eigenes Modell, das sogenannte Wendelsteiner Modell. In der zahlreichen familienrechtlichen Tagungen und in Zusammenarbeit mit der Lutherischen Tagungshaus Kirchwald, dem Bundesweiten Sorgerechtskongress wurden auf zahlreichen weiteren Tagungen die Forderungen des NEKV über eine eigenständige Vertretung des Kindes in familiengerichtlichen Verfahren schließlich durch die Erschaffung eines Verfahrensbeistandes Gesetz.
Das Nordische Elternschutzkreis entwickelte diverse Modelle außergerichtlicher Konfliktlösungen, was auch heute noch zentraler Bestandteil seiner Arbeit ist.
The Nordic Parental Care Circle (NEKV) is a registered association that was founded in 1982.
The Nordic Parental Care Circle eV is committed to family rights, especially children. From the beginning, the Nordic parental care circle maintained an advice center in Stuttgart and developed its own model from its many years of activity, the so-called Wendelstein model. In numerous family law conferences and in cooperation with the Lutherische Tagungshaus Kirchwald, the National Custody Congress, the NEKV's demands for an independent representation of the child in family court proceedings were finally met at numerous other conferences by the creation of a procedural lawyer.
The Nordic Parental Care Circle developed various models of out-of-court conflict resolution, which is still a central part of its work today.
Aufgabenstellung
Überarbeitung des NEKV-Logos + Erstellung des Corporate Designs
Das Logo symbolisiert das Kind im Mittelpunkt elterlicher und staatlicher Fürsorge. Eine Auffrischung dieses Logos entsprechend dem dynamischen Auftrag und der Aufgabe des NEKV ist dringend notwendig. Nach wie vor sieht sich das NEKV als ein Sachwalter der Interessen des Kindes als eine moderne Institutionen, die nunmehr auf eine fast vierzigjährige Tätigkeit zurückblicken kann.
Revision of the NEKV-Logo + creation of the corporate design
The logo symbolizes the child in the center of parental and state care. It is urgently necessary to refresh this logo in accordance with the dynamic mandate and the task of the NEKV. As before, the NEKV sees itself as an administrator of the interests of the child as a modern institution that can now look back on almost 40 years of activity.

```html
<!DOCTYPE html>
<html lang="de">
<head>
<meta charset="utf-8">
<title>Nordisches Elternschutzkreis e. V. – Visitenkarte</title>
<link href="https://fonts.googleapis.com/css2?family=Roboto:wght@400;500;700&display=swap" rel="stylesheet">
<style>
  :root {
    --page-bg: #ececed;
    --card-bg: #ffffff;
    --brand-blue: #1a9be0;
    --brand-blue-light: #8fd0f2;
    --rule-blue: #6cc3ee;
    --text-dark: #333638;
    --text-mid: #555a5e;
  }
  * { margin: 0; padding: 0; box-sizing: border-box; }
  html, body {
    width: 1116px;
    height: 1200px;
    overflow: hidden;
    background: var(--page-bg);
    font-family: "Roboto", Arial, sans-serif;
  }
  .sheet {
    position: relative;
    width: 1116px;
    height: 1200px;
  }
  .card {
    position: absolute;
    left: 178px;
    width: 760px;
    height: 492px;
    background: var(--card-bg);
    box-shadow: 0 3px 10px rgba(0,0,0,0.18);
    overflow: hidden;
  }
  .card--contact { top: 70px; }
  .card--brand { top: 638px; }

  /* contact side */
  .seal {
    position: absolute;
    left: 552px;
    top: 52px;
    width: 152px;
    height: 152px;
    border: 3px solid var(--brand-blue);
    border-radius: 50%;
    display: flex;
    align-items: center;
    justify-content: center;
    color: var(--brand-blue);
    font-weight: 500;
    font-size: 22px;
    letter-spacing: 1px;
  }
  .person__name {
    position: absolute;
    left: 43px;
    top: 132px;
    font-size: 32px;
    font-weight: 700;
    color: var(--brand-blue);
  }
  .person__role {
    position: absolute;
    left: 43px;
    top: 180px;
    font-size: 19px;
    color: var(--text-dark);
  }
  .divider {
    position: absolute;
    left: 43px;
    top: 230px;
    width: 680px;
    height: 2px;
    background: var(--rule-blue);
  }
  .contact-list {
    position: absolute;
    left: 43px;
    top: 262px;
    list-style: none;
  }
  .contact-list li {
    display: flex;
    align-items: center;
    height: 31px;
    font-size: 20px;
    color: var(--text-mid);
  }
  .contact-list svg {
    width: 22px;
    height: 22px;
    margin-right: 12px;
    flex: none;
  }
  .address {
    position: absolute;
    right: 44px;
    top: 323px;
    text-align: right;
    font-size: 20px;
    line-height: 31px;
    color: var(--text-mid);
  }
  .footer-bands {
    position: absolute;
    left: 0;
    bottom: 0;
    width: 760px;
    height: 36px;
  }

  /* brand side */
  .brand {
    position: absolute;
    inset: 0;
    display: flex;
    align-items: center;
    justify-content: center;
    gap: 38px;
  }
  .brand__dot {
    width: 160px;
    height: 160px;
    border-radius: 50%;
    background: var(--brand-blue);
    flex: none;
  }
  .brand__name {
    font-size: 33px;
    font-weight: 400;
    line-height: 40px;
    letter-spacing: 1px;
    color: var(--text-dark);
  }
</style>
</head>
<body>
<main class="sheet">

  <section class="card card--contact" aria-label="Visitenkarte Rückseite">
    <div class="seal">NEKV e. V.</div>

    <h1 class="person__name">Muster Musterson</h1>
    <p class="person__role">Geschäftsführung</p>
    <div class="divider"></div>

    <ul class="contact-list">
      <li>
        <svg viewBox="0 0 22 22" aria-hidden="true"><circle cx="11" cy="11" r="11" fill="var(--brand-blue)"/><path d="M11 5a4 4 0 0 0-4 4c0 3 4 8 4 8s4-5 4-8a4 4 0 0 0-4-4zm0 5.5a1.5 1.5 0 1 1 0-3 1.5 1.5 0 0 1 0 3z" fill="#fff"/></svg>
        +49 4411 20934
      </li>
      <li>
        <svg viewBox="0 0 22 22" aria-hidden="true"><circle cx="11" cy="11" r="11" fill="var(--brand-blue)"/><path d="M8 5.5l2 2.5-1.2 1.5c.7 1.5 1.9 2.7 3.4 3.4L13.7 11.7l2.5 2-1 1.8c-4.5-.3-8.2-4-8.5-8.5z" fill="#fff"/></svg>
        +49 160 98765432
      </li>
      <li>
        <svg viewBox="0 0 22 22" aria-hidden="true"><circle cx="11" cy="11" r="11" fill="var(--brand-blue)"/><rect x="6" y="7.5" width="10" height="7" rx="1" fill="#fff"/><path d="M6.5 8l4.5 3.5L15.5 8" stroke="var(--brand-blue)" stroke-width="1.2" fill="none"/></svg>
        info@elternschutzkreis.example
      </li>
      <li>
        <svg viewBox="0 0 22 22" aria-hidden="true"><circle cx="11" cy="11" r="11" fill="var(--brand-blue)"/><circle cx="11" cy="11" r="5" stroke="#fff" stroke-width="1.2" fill="none"/><path d="M6 11h10M11 6c-2 3-2 7 0 10M11 6c2 3 2 7 0 10" stroke="#fff" stroke-width="1.1" fill="none"/></svg>
        www.elternschutzkreis.example
      </li>
    </ul>

    <p class="address">Lindenweg 17<br>24103 Kirchwald</p>

    <svg class="footer-bands" viewBox="0 0 760 36" preserveAspectRatio="none" aria-hidden="true">
      <rect x="0" y="19" width="760" height="17" fill="var(--brand-blue-light)"/>
      <polygon points="553,36 580,4 760,4 760,36" fill="var(--brand-blue)"/>
    </svg>
  </section>

  <section class="card card--brand" aria-label="Visitenkarte Vorderseite">
    <div class="brand">
      <div class="brand__dot" aria-hidden="true"></div>
      <p class="brand__name">NORDISCHES<br>ELTERNSCHUTZKREIS<br>e. V.</p>
    </div>
  </section>

</main>
</body>
</html>
```